nutrition ebook cover

i need a cover for a ebook designed, the book is called Amber Lattice so i would like that somewhere on the cover. i would also like the word nutrition followed by my company logo that i have attached below somewhere on the cover( i have attached two logos and would like to see with both separatley), i would like this to be faded into the background if possible, perhaps in a upper or lower corner. i would also like to see options with and without the picture i have attached below. the look I'm going for is professional and clean. this is a fat loss, healthy eating booklet. the winning designer i would like to design the following pages within the book aswell no more than 10 pages, that i will provide all content for, i just need help with putting what i have on pdf in a way that looks professional and cool. this would ideally covered in the rate that is paid for the cover. i also have other booklets i need made so the winning designer will most likely get that work too at a later date for an additional fee of course.

Industry/Entity Type

Nutrition

Requirements
Nice to have
• Outside images are welcomed, happy to purchase any stock images used from a outside source

```html
<!DOCTYPE html>
<html lang="en">
<head>
<meta charset="utf-8">
<title>Amber Lattice — Nutrition Booklet</title>
<link rel="stylesheet" href="https://fonts.googleapis.com/css2?family=Lato:wght@100;300;400;700&display=swap">
<style>
  :root {
    --backdrop: #e9e9e9;
    --ink-dark: #262223;
    --brand-red: #d42229;
    --paper: #ffffff;
    --text: #2b2b2b;
    --photo-dark: #2f3b3d;
    --photo-wood: #8a5a3a;
    --photo-green: #4f7a3a;
  }
  * { box-sizing: border-box; margin: 0; padding: 0; }
  html, body { width: 987px; height: 1200px; overflow: hidden; background: var(--backdrop); }
  body { position: relative; font-family: 'Lato', sans-serif; color: var(--text); }

  /* ---------- Cover ---------- */
  .cover { position: absolute; left: 283px; top: 19px; width: 435px; height: 564px; background: var(--ink-dark); }
  .brand-mark { position: absolute; top: 52px; left: 0; width: 100%; display: flex; justify-content: center; align-items: center; gap: 8px; }
  .brand-mark .dot { width: 14px; height: 14px; border-radius: 50%; background: var(--paper); }
  .brand-mark .name { color: var(--paper); font-weight: 400; font-size: 15px; letter-spacing: 3px; text-transform: uppercase; }
  .cover-photo { position: absolute; top: 117px; left: 0; width: 100%; height: 330px;
    background: radial-gradient(ellipse at 50% 50%, var(--photo-wood) 0%, #6b4a32 30%, var(--photo-dark) 58%),
                linear-gradient(90deg, var(--photo-green), var(--photo-dark) 40%, var(--photo-dark) 60%, var(--photo-green)); background-blend-mode: normal; }
  .cover-title { position: absolute; top: 270px; left: 0; width: 100%; text-align: center; }
  .cover-title span { display: inline-block; padding: 4px 10px; border: 1px solid var(--ink-dark); color: var(--ink-dark);
    font-weight: 300; font-size: 32px; line-height: 1; }
  .cover-label { position: absolute; top: 476px; left: 0; width: 100%; display: flex; justify-content: center; }
  .cover-label span { color: var(--paper); font-weight: 400; font-size: 17px; letter-spacing: 5px; padding: 2px 12px;
    border-left: 1px solid var(--brand-red); border-right: 1px solid var(--brand-red); }

  /* ---------- Spread ---------- */
  .spread { position: absolute; left: 58px; top: 610px; width: 870px; height: 562px; display: flex; }
  .page { position: relative; width: 435px; height: 100%; }
  .page-contents { background: var(--brand-red); color: var(--paper); }
  .page-plan { background: var(--paper); }

  .contents-title { position: absolute; left: 84px; top: 62px; font-weight: 100; font-size: 47px; line-height: 1; }
  .toc { position: absolute; left: 83px; top: 130px; width: 268px; list-style: none; }
  .toc li { display: flex; align-items: baseline; font-weight: 300; font-size: 12px; height: 22px; }
  .toc .leader { flex: 1; border-bottom: 1px dotted var(--paper); margin: 0 2px; transform: translateY(-3px); }

  .disclaimer { position: absolute; left: 83px; top: 437px; width: 270px; border: 1px solid #f2a33a; padding: 6px 7px 5px; }
  .disclaimer h3 { font-size: 9.5px; font-weight: 700; }
  .disclaimer p { font-size: 5.6px; line-height: 1.5; font-weight: 700; }

  .plan-title { position: absolute; left: 49px; top: 62px; font-weight: 100; font-size: 47px; line-height: 1; color: var(--brand-red); }
  .plan-body { position: absolute; left: 49px; top: 117px; width: 320px; font-size: 7.3px; line-height: 1.55; }
  .plan-body p { margin-bottom: 9px; }
  .plan-body .accent { color: var(--brand-red); font-weight: 700; }
  .guidelines-title { color: var(--brand-red); font-size: 11.5px; font-weight: 400; margin: 8px 0 6px; }
  .guidelines { list-style: none; }
  .guidelines li { position: relative; padding-left: 12px; margin-bottom: 7.5px; }
  .guidelines li::before { content: ""; position: absolute; left: 0; top: 0; width: 7px; height: 7px; border: 1px solid var(--brand-red); border-radius: 50%; }
  .folio { position: absolute; left: 202px; top: 516px; font-size: 15px; font-weight: 300; padding: 0 8px;
    border-left: 1px solid var(--brand-red); border-right: 1px solid var(--brand-red); }
</style>
</head>
<body>

<section class="cover">
  <div class="brand-mark"><span class="dot"></span><span class="name">Kestrel Fitness</span></div>
  <div class="cover-photo" role="img" aria-label="Overhead photo of a wooden chopping board surrounded by fresh vegetables, mushrooms, tomatoes and herbs on a dark slate surface"></div>
  <div class="cover-title"><span>Amber Lattice</span></div>
  <div class="cover-label"><span>nutrition</span></div>
</section>

<section class="spread">
  <div class="page page-contents">
    <h1 class="contents-title">Contents</h1>
    <ul class="toc">
      <li>The Plan and Your Guidelines<span class="leader"></span>1</li>
      <li>Your Plate<span class="leader"></span>2</li>
      <li>Foods to Avoid<span class="leader"></span>3</li>
      <li>Greens<span class="leader"></span>4</li>
      <li>Fats<span class="leader"></span>5</li>
      <li>Protein<span class="leader"></span>6</li>
      <li>Carbohydrates<span class="leader"></span>7</li>
      <li>Extras<span class="leader"></span>8</li>
      <li>Helpful Tips<span class="leader"></span>9</li>
    </ul>
    <div class="disclaimer">
      <h3>Disclaimer</h3>
      <p>These guidelines are not intended to treat any medical condition and are intended for healthy individuals. If you have any doubts on whether this plan is right for you, consult a doctor before you begin. Everyone has the responsibility to assess the guidelines provided and make an informed personal decision to follow them. Kestrel Fitness accepts no liability for anyone following this plan.</p>
    </div>
  </div>

  <div class="page page-plan">
    <h1 class="plan-title">The Plan</h1>
    <div class="plan-body">
      <p>Nutrition is the backbone to any healthy lifestyle. Without smart nutrition, all of your hard work and best intentions in the gym will fall by the wayside. Eating well plays a vital role not only with fat loss, but also with your all around wellbeing. What you feed your body significantly influences your energy levels, sleep quality, concentration, digestion, immune system etc.</p>
      <p>The <span class="accent">Amber Lattice Nutrition Plan</span> has been developed to guide you towards leading a healthy and sustainable lifestyle. There is nothing scary or extreme about this plan – everything prescribed here is based on eating whole and natural foods, cutting out foods you may have intolerances to, and eliminating processed foods that your body isn't designed to handle. This plan is designed to help you look and feel better whilst creating healthy habits that will stay with you long term.</p>
      <p>I hope that by the end of the 28 days you will have established a strong understanding on the importance of eating well and how rewarding this can be.</p>
      <p>You will have developed healthy and sustainable eating habits, creating a new "normal" baseline that will bring you closer to your goals.</p>
      <h2 class="guidelines-title">Your Guidelines</h2>
      <ul class="guidelines">
        <li>Eat every 2-3 hours.</li>
        <li>No snacking. Every time you eat, it is a meal.</li>
        <li>Eat before you get hungry.</li>
        <li>Don't skip meals.</li>
        <li>Stop eating before you get full.</li>
        <li>Eat your last meal at least 2 hours before bed.</li>
        <li>Drink a minimum of 40ml of water per kg of your<br>bodyweight per day (i.e. 80kg person to drink 3.2L a day).</li>
        <li>Sleep 7-9 hours a night.</li>
      </ul>
    </div>
    <div class="folio">1</div>
  </div>
</section>

</body>
</html>
```